Surface Protection company needs cards

We are a New Zealand company that will apply nanotechnology coatings on surfaces to prevent growth and spread of bacteria, viruses, mold etc with a sprayer. We deal with large corporates, airlines, hospitals and schools so we are after a new modern, simple and clean look that will have great visual impact.
We a company that is focused on prevention and protection.

Company name, Vela Shield

Subtext, Antimicrobial Surface Protection

Logo, VS

Target Market(s)

Hospitals, Transport agencies, Airlines, Corporate entities

Contact Information for Business Card

Company name, VelaShield
Logo, VS

Gareth Tolley
velashieldnz@postbox.example
+64219305562
www.velashield.example.nz

Requirements
Must have
• Simple clean look.
Nice to have
• We apply nano coatings so try and incorporate this into a theme somehow

```html
<!DOCTYPE html>
<html lang="en">
<head>
<meta charset="utf-8">
<title>VelaShield Business Cards</title>
<link rel="stylesheet" href="https://fonts.googleapis.com/css2?family=Saira+Condensed:wght@400;500;600;700&display=swap">
<style>
  :root {
    --blue: #0a8fe0;
    --black: #1c1c1c;
    --white: #f4f4f4;
    --ghost: #e6e6e6;
    --grey-text: #8a8a8a;
    --bg: #e4e4e4;
    --font: "Saira Condensed", "Arial Narrow", sans-serif;
  }
  * { box-sizing: border-box; margin: 0; padding: 0; }
  html, body { width: 1200px; height: 900px; overflow: hidden; }
  body {
    background: var(--bg);
    font-family: var(--font);
    display: flex;
    align-items: center;
    justify-content: center;
    gap: 60px;
  }
  .card {
    width: 520px;
    height: 297px;
    position: relative;
    overflow: hidden;
    box-shadow: 0 10px 30px rgba(0,0,0,0.12);
  }

  /* Front */
  .card--front { background: var(--blue); }
  .front__brand {
    position: absolute;
    left: 0; right: 0; top: 52px;
    padding: 0 32px;
    text-align: center;
    white-space: nowrap;
    color: #fff;
    font-weight: 600;
    font-size: 96px;
    line-height: 1;
    letter-spacing: 2px;
  }
  .front__band {
    position: absolute;
    left: 0; right: 0; bottom: 0;
    height: 96px;
    background: var(--black);
  }
  .front__tagline {
    position: absolute;
    left: 40px; top: 14px;
    color: #fff;
    font-size: 15px;
    font-weight: 500;
    letter-spacing: 1.5px;
    text-transform: uppercase;
  }

  /* Back */
  .card--back { background: var(--white); }
  .back__ghost-name {
    position: absolute;
    left: 0; right: 0; top: 86px;
    text-align: center;
    font-size: 74px;
    font-weight: 700;
    color: var(--ghost);
    line-height: 1;
    letter-spacing: 3px;
    white-space: nowrap;
    text-transform: uppercase;
  }
  .back__name {
    position: absolute;
    left: 0; right: 0; top: 76px;
    text-align: center;
    color: var(--blue);
    font-size: 34px;
    font-weight: 600;
    letter-spacing: 1px;
    text-transform: uppercase;
  }
  .back__band {
    position: absolute;
    left: 0; right: 0; top: 138px;
    height: 34px;
    background: var(--black);
    display: flex;
    align-items: center;
    justify-content: center;
    color: var(--grey-text);
    font-size: 14px;
    letter-spacing: 1.5px;
    text-transform: uppercase;
    white-space: nowrap;
  }
  .back__contacts {
    position: absolute;
    left: 0; right: 0; top: 172px; bottom: 0;
    background: var(--blue);
    display: flex;
    justify-content: space-between;
    align-items: flex-start;
    padding: 26px 24px 0;
  }
  .contact {
    display: flex;
    flex-direction: column;
    align-items: center;
    gap: 12px;
    color: #fff;
    font-size: 12px;
    letter-spacing: 0.8px;
    text-transform: uppercase;
    white-space: nowrap;
  }
  .contact__icon {
    width: 20px; height: 20px;
    background: var(--black);
    display: flex; align-items: center; justify-content: center;
  }
</style>
</head>
<body>

<section class="card card--front" aria-label="Card front">
  <div class="front__brand">VELASHIELD</div>
  <div class="front__band">
    <p class="front__tagline">Antimicrobial Surface Protection</p>
  </div>
</section>

<section class="card card--back" aria-label="Card back">
  <div class="back__ghost-name" aria-hidden="true">Gareth Tolley</div>
  <h1 class="back__name">Gareth Tolley</h1>
  <div class="back__band">VelaShield Antimicrobial Surface Protection</div>
  <div class="back__contacts">
    <div class="contact">
      <span class="contact__icon">
        <svg width="12" height="12" viewBox="0 0 24 24" aria-hidden="true"><path fill="#fff" d="M6.6 10.8a15 15 0 0 0 6.6 6.6l2.2-2.2c.3-.3.7-.4 1-.2 1.1.4 2.3.6 3.6.6.6 0 1 .4 1 1V20c0 .6-.4 1-1 1A17 17 0 0 1 3 4c0-.6.4-1 1-1h3.5c.6 0 1 .4 1 1 0 1.3.2 2.5.6 3.6.1.3 0 .7-.2 1z"/></svg>
      </span>
      <span>+64219305562</span>
    </div>
    <div class="contact">
      <span class="contact__icon">
        <svg width="12" height="12" viewBox="0 0 24 24" aria-hidden="true"><rect x="2" y="5" width="20" height="14" fill="none" stroke="#fff" stroke-width="2"/><path d="M2 5l10 8 10-8" fill="none" stroke="#fff" stroke-width="2"/></svg>
      </span>
      <span>velashieldnz@postbox.example</span>
    </div>
    <div class="contact">
      <span class="contact__icon">
        <svg width="12" height="12" viewBox="0 0 24 24" aria-hidden="true"><circle cx="12" cy="12" r="9" fill="none" stroke="#fff" stroke-width="2"/><path d="M3 12h18M12 3c3 3 3 15 0 18M12 3c-3 3-3 15 0 18" fill="none" stroke="#fff" stroke-width="1.6"/></svg>
      </span>
      <span>www.velashield.example.nz</span>
    </div>
  </div>
</section>

</body>
</html>
```